New Website for ReBranded Company - CrewBeacon

We have a successful company and website currently but it is a little dated. We have re-branded the company from Harbor Signal Networks to CrewBeacon and have a new logo for the new name. We are looking to build a newer fresher website with the new name. I will need a concept of the home page and one inside page. You can see our current site at https://www.harborsignalnetworks.example and the new site will be https://www.crewbeacon.example .

I also really like the https://www.pathlantern.example/ website. I like ledgerkite.example website. I like the https://skillorbit.example/ website.

See the attached document for layout and some text to use. Use the pictures I attached as opposed to pictures from the old site as much as you can.

Target Market(s)

Business

Industry/Entity Type

Software Service

Number of Pages Required

2 page

Font styles to use
Sans Serif

Requirements
Must have
• Use the colors from my logo. Professional but modern. We want people to feel like our product makes their staff feel safer at work.
Should not have
• Don't use any red or orange (no stop colors).

```html
<!DOCTYPE html>
<html lang="en">
<head>
<meta charset="utf-8">
<title>CrewBeacon — Feel Confident That Your Staff is Protected</title>
<link href="https://fonts.googleapis.com/css2?family=Source+Sans+3:wght@300;400;600;700&display=swap" rel="stylesheet">
<style>
:root{
  --blue:#2a86c7;
  --blue-wave:#3893d2;
  --green:#6ab244;
  --ink:#3d3d3d;
  --ink-soft:#555;
  --white:#fff;
}
*{margin:0;padding:0;box-sizing:border-box}
html,body{width:1200px;height:3700px;overflow:hidden}
body{font-family:"Source Sans 3",sans-serif;color:var(--ink);background:var(--white);position:relative}
section,header,footer{position:absolute;left:0;width:1200px}
.abs{position:absolute}
.btn{position:absolute;display:flex;align-items:center;justify-content:center;background:var(--blue);color:var(--white);font-size:14px;font-weight:600;border-radius:3px;text-decoration:none}
.btn--outline{background:var(--white);color:var(--blue);border:2px solid var(--blue)}
.green{color:var(--green);font-weight:600}
.ph{position:absolute}

/* brand name */
.brand{position:absolute;display:flex;align-items:center;gap:12px;font-size:44px;font-weight:600;color:var(--blue);line-height:1}
.brand__mark{width:18px;height:18px;border-radius:50%;background:var(--blue)}

/* header */
.site-header{top:0;height:125px;box-shadow:0 3px 8px rgba(0,0,0,.08);background:var(--white);z-index:2}
.nav{position:absolute;top:54px;font-size:15px;color:var(--ink)}
/* hero */
.hero{top:125px;height:486px}
.hero h1{position:absolute;left:127px;width:400px;top:82px;text-align:center;font-weight:300;font-size:34px;line-height:54px;color:var(--ink-soft)}
.hero p{position:absolute;left:87px;width:480px;top:207px;text-align:center;font-size:17px}
/* features */
.features{top:611px;height:488px;background:var(--blue)}
.feature{position:absolute;left:694px;width:365px;color:var(--white);font-size:17px;line-height:27px}
.feature b{display:block;font-weight:700}
.feature-icon{position:absolute;left:606px}
/* employees */
.employees{top:1099px;height:331px}
.employees h2{position:absolute;left:304px;width:800px;top:72px;text-align:center;font-weight:400;font-size:25px}
.employees p{position:absolute;left:304px;width:800px;top:132px;text-align:center;font-size:17px;line-height:27px}
/* why */
.why{top:1430px;height:507px;background:var(--blue);overflow:hidden;color:var(--white)}
.why h2{position:absolute;width:1200px;top:40px;text-align:center;font-weight:300;font-size:40px}
.why .lead{position:absolute;left:195px;width:810px;top:128px;text-align:center;font-size:17px;line-height:28px}
.why .col{position:absolute;width:340px;font-size:17px;line-height:27px}
.why .col small{display:block;font-size:13px;font-weight:700;line-height:22px}
/* worry */
.worry{top:1937px;height:453px}
.worry h2{position:absolute;left:125px;top:36px;width:530px;font-weight:300;font-size:33px;line-height:53px}
.worry p{position:absolute;left:125px;top:150px;width:330px;font-size:17px;line-height:28px}
.stat{position:absolute;color:var(--blue);text-align:center}
.stat b{display:block;font-size:42px;font-weight:600;line-height:1}
.stat span{font-size:24px}
/* plan */
.plan{top:2390px;height:746px}
.plan h2{position:absolute;left:525px;width:560px;top:46px;text-align:center;font-weight:300;font-size:40px}
.step-num{position:absolute;left:630px;width:80px;height:80px;border:4px solid var(--green);border-radius:50%;color:var(--green);font-size:40px;font-weight:600;display:flex;align-items:center;justify-content:center}
.step{position:absolute;left:734px;width:290px}
.step h3{font-weight:400;font-size:24px;line-height:28px;color:var(--ink-soft)}
.step p{font-size:13px;line-height:27px;margin-top:4px}
/* cta */
.cta{top:3136px;height:145px;background:var(--blue)}
.cta h2{position:absolute;left:195px;top:52px;color:var(--white);font-size:25px;font-weight:600}
/* footer */
.site-footer{top:3281px;height:419px}
.call{position:absolute;left:117px;width:320px;text-align:center}
.fcol{position:absolute;top:44px;width:160px;text-align:center;font-size:13px;line-height:27px}
.fcol h4{font-size:17px;color:var(--blue);font-weight:700;line-height:24px;margin-bottom:4px}
</style>
</head>
<body>

<header class="site-header">
  <div class="brand" style="left:125px;top:40px"><span class="brand__mark"></span>CrewBeacon</div>
  <span class="nav" style="left:549px">Home</span>
  <span class="nav" style="left:638px">Buy Addons</span>
  <span class="nav" style="left:760px">Customer Login &nbsp;⌄</span>
  <a class="btn" style="left:925px;top:45px;width:150px;height:37px;font-size:12px">Explore your Choices</a>
</header>

<section class="hero">
  <h1><span class="green">Feel Confident</span> That Your Staff is Protected</h1>
  <p>Get a revolutionary new electronic panic button</p>
  <a class="btn" style="left:224px;top:279px;width:204px;height:49px">Ready To Get Started</a>
  <div class="ph" role="img" aria-label="Laptop and phone showing the alert dashboard" style="left:565px;top:37px;width:635px;height:408px;background:linear-gradient(135deg,#e9edf1,#c9d2da);border-radius:10px"></div>
</section>

<section class="features">
  <div class="ph" role="img" aria-label="Desk phone beside a two-button panic device" style="left:0;top:0;width:543px;height:488px;background:linear-gradient(160deg,#b7ada0,#6e665e 60%,#2e2c2b)"></div>
  <svg class="feature-icon" style="top:74px" width="38" height="38" viewBox="0 0 38 38"><circle cx="19" cy="19" r="15" fill="none" stroke="#fff" stroke-width="4"/><line x1="9" y1="9" x2="29" y2="29" stroke="#fff" stroke-width="4"/></svg>
  <div class="feature" style="top:61px"><b>Problems Stopped</b>Before They Start For Any Type Of Organization</div>
  <svg class="feature-icon" style="top:210px" width="38" height="44" viewBox="0 0 38 44"><text x="19" y="38" text-anchor="middle" font-size="44" font-weight="700" fill="#fff" font-family="Source Sans 3,sans-serif">$</text></svg>
  <div class="feature" style="top:190px"><b>Affordable Prices</b>Starting at $18 per month. No Contracts. No Hidden Costs.</div>
  <svg class="feature-icon" style="top:364px" width="38" height="38" viewBox="0 0 38 38"><path d="M19 5c-6 0-10 4-10 10v8l-4 5h28l-4-5v-8c0-6-4-10-10-10z" fill="#fff"/><circle cx="19" cy="32" r="3.5" fill="#fff"/><path d="M4 12a12 12 0 0 1 4-6M34 12a12 12 0 0 0-4-6" stroke="#fff" stroke-width="2.5" fill="none"/></svg>
  <div class="feature" style="top:339px"><b>Alerts</b>By computer, mobile device, text, phone, email, monitoring and E911</div>
</section>

<section class="employees">
  <div class="ph" role="img" aria-label="Employee wearing a panic button pendant" style="left:128px;top:84px;width:184px;height:184px;border-radius:50%;background:radial-gradient(circle at 50% 60%,#2b3440,#151a22);box-shadow:0 4px 14px rgba(0,0,0,.2)"></div>
  <h2>Your Employees Shouldn’t Feel Alone When They Need <b>Help</b></h2>
  <p>Does this problem make you feel frustrated and anxious?<br>Put a <span class="green">simple solution</span> in their hands</p>
  <a class="btn" style="left:602px;top:232px;width:204px;height:49px">Ready To Get Started</a>
</section>

<section class="why">
  <svg class="abs" style="left:0;top:0" width="1200" height="507" viewBox="0 0 1200 507"><path d="M-40 200C40 20 220 10 300 120 370 220 300 400 160 507H-40Z" fill="var(--blue-wave)"/><path d="M1240 120C1100 150 1000 230 900 330 860 400 900 507 960 507H1240Z" fill="var(--blue-wave)"/></svg>
  <h2>Why <b style="font-weight:700">Businesses</b> Choose Us</h2>
  <div class="lead"><b>Easy to Use</b><br>Press a button and let the right people know you need help and open a chat window letting everyone talk on resolving their problem.</div>
  <div class="ph" role="img" aria-label="Phone displaying the app icon" style="left:539px;top:241px;width:109px;height:235px;background:linear-gradient(#f4f7fa,#dfe7ee);border:7px solid #1b1b1b;border-radius:14px"></div>
  <div class="col" style="left:165px;top:327px"><b>Comunicate the Way You Want</b><small>We give you lots of options:</small>Computer, Mobile, Email, Phone call, Text, E911, Call Center</div>
  <div class="col" style="left:713px;top:327px"><b>Cost Effective Protection</b><br>By leveraging your existing network and equipment we can lower your costs to give better options to your staff.</div>
</section>

<section class="worry">
  <h2>We know how scary it can feel to worry about <span class="green">employee safety</span></h2>
  <p>That’s why we have provided a way for customers to get help to staff effectively in</p>
  <div class="stat" style="left:125px;top:226px"><b>45</b><span>States</span></div>
  <span class="abs" style="left:262px;top:244px;font-size:22px">covering</span>
  <div class="stat" style="left:401px;top:226px"><b>5</b><span>Countries</span></div>
  <a class="btn" style="left:126px;top:344px;width:203px;height:49px">Start My Demo</a>
  <div class="ph" role="img" aria-label="Hand pressing a button mounted under a desk" style="left:704px;top:0;width:496px;height:453px;background:linear-gradient(160deg,#6f6a60,#9b9386 45%,#5d5850)"></div>
</section>

<section class="plan">
  <div class="ph" role="img" aria-label="Hand pulling a panic button from a jeans pocket" style="left:0;top:0;width:525px;height:746px;background:linear-gradient(170deg,#2f4b75,#3f6396 50%,#23385a)"></div>
  <h2><b style="font-weight:700">Simple</b> Start Plan</h2>
  <div class="step-num" style="top:129px">1</div>
  <div class="step" style="top:136px"><h3><span class="green">Explore</span> Your Choices</h3><p>Pricing, Trial, Quote, Hardware</p></div>
  <div class="step-num" style="top:267px">2</div>
  <div class="step" style="top:271px;width:250px"><h3><span class="green">Get</span> Setup</h3><p>Input Your Alerts, Input Your Staff, Install Our Software</p></div>
  <div class="step-num" style="top:414px">3</div>
  <div class="step" style="top:432px;width:285px"><h3><span class="green">Feel Confident</span> Your Staff is Protected</h3><p style="width:215px">High Five. You just too a major step to getting rid of the anxiety and frustration this gave you.</p></div>
  <a class="btn btn--outline" style="left:700px;top:636px;width:203px;height:49px">Start My Demo</a>
</section>

<section class="cta">
  <h2>Stay Connected with Staff during a Crisis Situations</h2>
  <a class="btn btn--outline" style="left:832px;top:47px;width:203px;height:49px;border-color:#fff">Start My Demo</a>
</section>

<footer class="site-footer">
  <div class="call" style="top:40px;font-size:22px;color:var(--blue)">CALL <b>US</b></div>
  <div class="call" style="top:92px;font-size:23px;color:var(--blue);font-weight:700">1 – 800 – 555 – 0142</div>
  <div class="call" style="top:150px;font-size:13px;line-height:27px">When employees feel alone during a threatening situation, we give them a way to let the right resources know that they need help so you can feel confident that your staff is protected.</div>
  <div class="brand" style="left:152px;top:316px;font-size:40px"><span class="brand__mark"></span>CrewBeacon</div>
  <div class="call" style="top:376px;font-size:10px;color:var(--blue)">©CrewBeacon 2020</div>

  <div class="fcol" style="left:496px"><h4>Shop</h4>Add Ons<br>Start My Demo<br>Custom Quote<br>Start Trial</div>
  <div class="fcol" style="left:654px"><h4>About</h4>Affiliates<br>Contact<br>Support<br>Existing Customers<br>Industries<br>Blog<br>FAQ</div>
  <div class="fcol" style="left:810px"><h4>Legal</h4>Privacy Policy<br>Terms of Use<br>End User License<br>Agreement</div>
  <svg class="abs" style="left:993px;top:49px" width="20" height="20" viewBox="0 0 20 20"><circle cx="10" cy="10" r="10" fill="var(--blue)"/><path d="M5.5 12l4.5-4.5 4.5 4.5" stroke="#fff" stroke-width="2.4" fill="none"/></svg>

  <span class="abs" style="left:533px;top:342px;width:16px;height:16px;border-radius:50%;background:var(--blue)"></span>
  <span class="abs" style="left:575px;top:342px;width:16px;height:16px;border-radius:50%;background:var(--blue)"></span>
  <svg class="abs" style="left:533px;top:377px" width="16" height="11" viewBox="0 0 16 11"><rect width="16" height="11" rx="1.5" fill="var(--blue)"/><path d="M1 1l7 5 7-5" stroke="#fff" stroke-width="1.4" fill="none"/></svg>
  <span class="abs" style="left:556px;top:374px;font-size:11px">info@harborsignalnetworks.example</span>
</footer>

</body>
</html>
```